TOLMERY EU Project PowerPoint Template

Please Provide a PowerPoint template to be used for a European project. The main scope of the project is to support research organisations across Europe to design and implement gender equality plans in order to promote the women’s position of the filed of STEM research.
The Power Point template is going to be used by the entire consortium of the project (approx. 50 people) and it is going to be used to deliver official reports to the Halvren Oversight Board and in real -life events like international Conferences etc. Therefore, the design has to be professional and official. Given that the PowerPoint template is going to be utilised by several people simultaneously, the document should afford each user to add elements (tables, etc.) that have the same format. Any time the user adds bullet points, these should have a particular colour and shape, and so on. Please note the Consortium members are both MS Windows and MAC users.
In terms of layout, please consult the colour combination of the attached logo, to design a template with matching colour patterns. Attached to this project description you may find a generic PowerPoint template for the project just as an example. Pay notice to the bottom of each slide, where a specific phrase along with the EU flag must be included. Please, keep the phrase as it is; you my find images for the EU flag here: https://verdalinx.org/about-us/insignia/banner_en.
In addition, two more presentation templates from previous projects are provided as examples. You may have a good look at them too.
For any questions and/or clarifications feel free to contact.

```html
<!DOCTYPE html>
<html lang="en">
<head>
<meta charset="utf-8">
<title>TOLMERY – Presentation Deck</title>
<link rel="stylesheet" href="https://fonts.googleapis.com/css2?family=Montserrat:wght@300;400;500;600;700;800;900&display=swap">
<style>
:root{
  --purple:#5b4fa6;
  --purple-deep:#4a3f93;
  --purple-2:#7c72bf;
  --lilac:#a79fd6;
  --lilac-soft:#ecebf6;
  --yellow:#f2b600;
  --yellow-2:#f6cf6a;
  --ink:#222;
  --grey:#666;
  --muted:#8a8a96;
  --page:#e9e9ee;
  --flag:#1d3f99;
}
*{box-sizing:border-box;margin:0;padding:0}
html,body{width:1200px;height:2472px;overflow:hidden}
body{font-family:"Montserrat",sans-serif;color:var(--ink);background:var(--page)}
.canvas{position:relative;width:1200px;height:2472px;overflow:hidden;background:var(--page)}

/* hero */
.hero-photo{position:absolute;left:0;top:0}
.hero-brand{position:absolute;left:0;right:0;top:78px;display:flex;align-items:center;justify-content:center;gap:16px}
.hero-brand .dot{width:52px;height:52px;border-radius:50%;background:var(--yellow)}
.hero-brand .name{font-weight:500;font-size:64px;letter-spacing:2px;color:var(--purple);line-height:1}
.hero-title{position:absolute;left:70px;top:292px;width:400px;text-align:right}
.hero-title .big{display:block;font-weight:800;font-size:63px;color:var(--purple);line-height:1;letter-spacing:-.5px}
.hero-title .deck{display:block;font-weight:400;font-size:60px;color:#111;line-height:1.05;text-align:center;margin-left:40px}
.hero-slide{position:absolute;left:563px;top:192px;width:353px;height:199px;transform:scale(1.325);transform-origin:0 0}
.divider{position:absolute;left:462px;top:641px;width:254px;height:1px;background:#b9b6c8}
.section-title{position:absolute;left:0;right:0;top:670px;text-align:center;font-weight:400;font-size:33px;color:var(--purple-2)}

/* slide shell */
.slide{position:absolute;width:353px;height:199px;background:#fff;box-shadow:0 2px 6px rgba(40,30,90,.18);overflow:hidden}
.brand{position:absolute;top:7px;right:9px;display:flex;align-items:center;gap:3px;font-weight:600;font-size:7px;color:var(--purple);letter-spacing:.3px}
.brand::before{content:"";width:6px;height:6px;border-radius:50%;background:var(--yellow)}
.funding{position:absolute;left:6px;bottom:4px;display:flex;align-items:center;gap:4px;font-size:3px;color:#444;white-space:nowrap}
.funding i{display:block;width:9px;height:6px;background:var(--flag)}
.page-dot{position:absolute;right:8px;bottom:4px;width:9px;height:9px;border-radius:50%;border:1.5px solid var(--yellow)}
.title{position:absolute;left:0;right:0;top:16px;text-align:center;font-weight:700;font-size:15px;color:var(--purple)}
.subtitle{position:absolute;left:0;right:0;top:35px;text-align:center;font-weight:500;font-size:5px;letter-spacing:2.4px;color:var(--grey)}
.tiny{font-size:4px;line-height:5.2px;color:#555}
.tiny b{color:#222}
.abs{position:absolute}
.photo{position:absolute}

.agenda-word{position:absolute;font-weight:700;font-size:16px;color:var(--purple)}
.agenda-list{position:absolute;list-style:none;font-size:4.5px;color:var(--muted);line-height:12.5px}
.agenda-list span{display:inline-block;width:20px}

.card{position:absolute;background:#fff;box-shadow:0 1px 4px rgba(40,30,90,.2);text-align:center;padding:12px 5px 0}
.card h4{font-size:4.5px;font-weight:700;margin-bottom:2px}
.icon-ring{position:absolute;left:50%;top:-8px;margin-left:-8px;width:16px;height:16px;border-radius:50%;background:#fff;border:1.5px solid var(--purple);box-shadow:0 1px 2px rgba(0,0,0,.15)}

.num{position:absolute;width:12px;height:12px;border-radius:50%;background:var(--purple);color:#fff;font-size:5px;font-weight:700;display:flex;align-items:center;justify-content:center}

.grid-table{position:absolute;border-collapse:collapse;font-size:3.6px;color:#555;text-align:center}
.grid-table td,.grid-table th{height:11px;padding:0}
.grid-table th{background:var(--purple-2);color:#fff;font-weight:600}
.grid-table tr:nth-child(even) td{background:#eeeeef}
.grid-table .accent td{background:var(--purple);color:#fff}

.badge{position:absolute;width:38px;height:24px;background:#fff;box-shadow:0 1px 3px rgba(0,0,0,.18);display:flex;align-items:center;justify-content:center}
.badge i{display:block;width:18px;height:7px;border-radius:1px}

.bullets{position:absolute;list-style:none;font-size:4px;line-height:5px;color:#444}
.bullets li{padding-left:6px;position:relative;margin-bottom:5px}
.bullets li::before{content:"";position:absolute;left:0;top:1px;width:3px;height:3px;background:var(--purple);transform:rotate(45deg)}
</style>
</head>
<body>
<main class="canvas">

  <svg class="hero-photo" width="1200" height="760" role="img" aria-label="Photo of a group of people silhouetted against a sunset sky, raising their hands, faded into the page">
    <defs>
      <linearGradient id="heroFade" x1="0" y1="0" x2="1" y2="1">
        <stop offset="0" stop-color="#b9c6d4"/>
        <stop offset=".45" stop-color="#c9c6cf"/>
        <stop offset="1" stop-color="#e9e9ee"/>
      </linearGradient>
    </defs>
    <polygon points="0,0 1200,0 1200,140 0,752" fill="url(#heroFade)"/>
  </svg>

  <div class="hero-brand">
    <div class="dot"></div>
    <div class="name">TOLMERY</div>
  </div>

  <h1 class="hero-title"><span class="big">Presentation</span><span class="deck">Deck</span></h1>

  <section class="slide hero-slide" style="box-shadow:none">
    <div class="brand">TOLMERY</div>
    <div class="title">Two Facts</div>
    <div class="subtitle">SUB TITLE GOES HERE</div>
    <div class="abs" style="left:38px;top:55px;font-size:38px;font-weight:900;color:var(--lilac);line-height:1">“</div>
    <div class="abs" style="left:40px;top:80px;width:112px;text-align:center;font-size:7.5px;font-weight:700;line-height:9px">GENDER EQUALITY IS NOT ONLY A MATTER OF SOCIAL JUSTICE BUT ALSO OF RESEARCH PERFORMANCE</div>
    <div class="photo" role="img" aria-label="Illustration of two figures holding linked gender symbols" style="left:200px;top:58px;width:135px;height:118px;background:radial-gradient(circle at 45% 55%,#d6d0f0,#f2dede 55%,#fff 80%)"></div>
    <div class="funding"><i></i>This project has received funding from the Halvren Oversight Board's Meridian research and innovation programme under Grant Agreement No 000000</div>
    <div class="page-dot" style="background:var(--purple);border-color:var(--purple)"></div>
  </section>

  <div class="divider"></div>
  <h2 class="section-title">Powerpoint Presentation</h2>

  <!-- Row 1 -->
  <section class="slide" style="left:48px;top:755px;background:linear-gradient(#fff 40%,#f3f2f9)">
    <div class="abs" style="left:0;top:0;width:353px;height:34px;border-bottom:2px solid var(--lilac-soft)"></div>
    <div class="abs" style="left:20px;top:20px;display:flex;align-items:center;gap:4px;font-weight:500;font-size:11px;color:var(--purple)"><span style="width:9px;height:9px;border-radius:50%;background:var(--yellow)"></span>TOLMERY</div>
    <div class="abs" style="left:133px;top:13px;font-size:5px;color:var(--purple)"><b>The TOLMERY project:</b><br>Linking research and innovation for gender equality</div>
    <div class="abs" style="left:100px;top:93px;width:170px;text-align:center">
      <div style="font-weight:700;font-size:15px;color:var(--purple)">Project Introduction</div>
      <div style="font-size:5px;letter-spacing:1px;color:var(--grey)">NAME, POSITION</div>
      <div style="font-size:3.8px;letter-spacing:1px;color:var(--grey)">LOCATION, DATE</div>
    </div>
    <div class="funding"><i></i>This project has received funding from the Halvren Oversight Board's Meridian research and innovation programme under Grant Agreement No 000000</div>
  </section>

  <section class="slide" style="left:423px;top:755px">
    <div class="photo" role="img" aria-label="Faded photo of people raising hands at sunset" style="inset:0;background:linear-gradient(180deg,#f4f4f8 0%,#dcdbe6 45%,#f6f6f9 100%)"></div>
    <div class="abs" style="left:0;right:0;top:13px;text-align:center;font-size:5px;color:var(--purple)"><b>The TOLMERY project:</b><br>Linking research and innovation for gender equality</div>
    <div class="abs" style="left:24px;top:68px;display:flex;align-items:center;gap:4px;font-weight:500;font-size:14px;color:var(--purple)"><span style="width:11px;height:11px;border-radius:50%;background:var(--yellow)"></span>TOLMERY</div>
    <div class="abs" style="left:24px;top:110px;font-weight:300;font-size:14px;color:var(--purple)">Project Introduction</div>
    <div class="abs" style="left:24px;top:131px;font-size:5px;letter-spacing:1px;color:var(--grey)">NAME, POSITION<br><span style="font-size:3.8px">LOCATION, DATE</span></div>
    <div class="funding"><i></i>This project has received funding from the Halvren Oversight Board's Meridian research and innovation programme under Grant Agreement No 000000</div>
  </section>

  <section class="slide" style="left:799px;top:755px">
    <div class="brand">TOLMERY</div>
    <div class="agenda-word" style="left:57px;top:88px">Agenda</div>
    <ol class="agenda-list" style="left:212px;top:32px">
      <li><span>i.</span>Introduction</li><li><span>ii.</span>About Us</li><li><span>iii.</span>Welcome Message</li><li><span>iv.</span>Company Profile</li><li><span>v.</span>Team</li><li><span>vi.</span>Team Group</li><li><span>vii.</span>Portfolio</li><li><span>viii.</span>Info graphic</li><li><span>ix.</span>Contact Us</li><li><span>x.</span>Data Chart</li>
    </ol>
    <div class="funding"><i></i>This project has received funding under Grant Agreement No 000000</div><div class="page-dot"></div>
  </section>

  <!-- Row 2 -->
  <section class="slide" style="left:48px;top:969px">
    <div class="brand">TOLMERY</div>
    <div class="agenda-word" style="left:56px;top:88px">Agenda</div>
    <ol class="agenda-list" style="left:212px;top:32px">
      <li><span>i.</span>Introduction</li><li><span>ii.</span>About Us</li><li><span>iii.</span>Welcome Message</li><li><span>iv.</span>Company Profile</li><li><span>v.</span>Team</li><li><span>vi.</span>Team Group</li><li><span>vii.</span>Portfolio</li><li><span>viii.</span>Info graphic</li><li><span>ix.</span>Contact Us</li><li><span>x.</span>Data Chart</li>
    </ol>
    <div class="funding"><i></i>This project has received funding under Grant Agreement No 000000</div><div class="page-dot"></div>
  </section>

  <section class="slide" style="left:423px;top:969px">
    <div class="photo" role="img" aria-label="Faded photo of people raising hands at sunset" style="left:0;top:0;width:353px;height:100px;background:linear-gradient(180deg,#dfe3ec,#f4f4f8)"></div>
    <div class="abs" style="left:24px;top:35px;display:flex;align-items:center;gap:3px;font-weight:500;font-size:10px;color:var(--purple)"><span style="width:8px;height:8px;border-radius:50%;background:var(--yellow)"></span>TOLMERY</div>
    <div class="abs" style="left:24px;top:64px;font-weight:700;font-size:11px;color:var(--purple)">Your Text Here</div>
    <p class="abs tiny" style="left:24px;top:92px;width:128px"><b>Lorem ipsum dolor sit amet,</b> consectetur adipiscing elit. Fusce sit amet neque sodales, faucibus ex eu, efficitur lacus. Cras imperdiet, nulla nec sagittis pulvinar, neque augue iaculis risus, ac fringilla felis urna fermentum mi. Ut vehicula vel enim sit amet vulputate. Aenean malesuada consectetur diam, ac convallis quam tincidunt eget.</p>
    <p class="abs tiny" style="left:190px;top:92px;width:135px"><b>Maecenas in purus at tellus tincidunt sodales eu sed nibh.</b> Aenean justo diam, commodo vel felis ac, malesuada sodales purus. Nunc sollicitudin sed justo in eleifend. Fusce dictum ornare ligula, eu porttitor elit ullamcorper non. Aliquam erat volutpat. Mauris malesuada turpis non tellus scelerisque tempus.</p>
    <div class="funding"><i></i>This project has received funding under Grant Agreement No 000000</div><div class="page-dot"></div>
  </section>

  <section class="slide" style="left:799px;top:969px">
    <div class="brand">TOLMERY</div>
    <div class="title">Two Column Text</div>
    <div class="subtitle">SUB TITLE GOES HERE</div>
    <p class="abs tiny" style="left:26px;top:52px;width:135px">Lorem ipsum dolor sit amet, consectetur adipiscing elit, sed do eiusmod tempor incididunt ut labore et dolore magna aliqua. Lorem ipsum dolor sit amet, consectetur adipiscing elit, sed do eiusmod tempor incididunt ut labore et dolore magna aliqua.<br><br>Lorem ipsum dolor sit amet, consectetur adipiscing elit, sed do eiusmod tempor incididunt ut labore et dolore magna aliqua. Lorem ipsum dolor sit amet, consectetur adipiscing elit.</p>
    <p class="abs tiny" style="left:192px;top:52px;width:135px">Lorem ipsum dolor sit amet, consectetur adipiscing elit, sed do eiusmod tempor incididunt ut labore et dolore magna aliqua. Lorem ipsum dolor sit amet, consectetur adipiscing elit, sed do eiusmod tempor incididunt ut labore et dolore magna aliqua.<br><br>Lorem ipsum dolor sit amet, consectetur adipiscing elit, sed do eiusmod tempor incididunt ut labore et dolore magna aliqua. Lorem ipsum dolor sit amet, consectetur adipiscing elit.</p>
    <div class="funding"><i></i>This project has received funding under Grant Agreement No 000000</div><div class="page-dot"></div>
  </section>

  <!-- Row 3 -->
  <section class="slide" style="left:48px;top:1184px">
    <div class="brand">TOLMERY</div>
    <div class="title">Two Facts</div>
    <div class="subtitle">SUB TITLE GOES HERE</div>
    <div class="abs" style="left:38px;top:55px;font-size:38px;font-weight:900;color:var(--lilac);line-height:1">“</div>
    <div class="abs" style="left:40px;top:82px;width:112px;text-align:center;font-size:7.3px;font-weight:700;line-height:9px">GENDER EQUALITY IS NOT ONLY A MATTER OF SOCIAL JUSTICE BUT ALSO OF RESEARCH PERFORMANCE</div>
    <div class="photo" role="img" aria-label="Illustration of two figures holding linked gender symbols" style="left:205px;top:55px;width:135px;height:120px;background:radial-gradient(circle at 45% 55%,#d6d0f0,#f2dede 55%,#fff 80%)"></div>
    <div class="funding"><i></i>This project has received funding under Grant Agreement No 000000</div><div class="page-dot"></div>
  </section>

  <section class="slide" style="left:423px;top:1184px">
    <div class="brand">TOLMERY</div>
    <div class="title">Bulleted List Text Sample</div>
    <div class="subtitle">SUB TITLE GOES HERE</div>
    <div class="photo" role="img" aria-label="Illustration of yellow and purple gender symbols" style="left:30px;top:52px;width:120px;height:118px;background:radial-gradient(circle at 35% 40%,#f6dc8a,#fff 45%),radial-gradient(circle at 70% 60%,#c9c2ea,#fff 50%)"></div>
    <div class="num" style="left:193px;top:58px">01</div>
    <p class="abs tiny" style="left:210px;top:50px;width:125px"><b>Your Text Here</b><br>You can simply impress your audience and add a unique zing and appeal to your Presentations.</p>
    <div class="num" style="left:193px;top:88px">02</div>
    <p class="abs tiny" style="left:210px;top:80px;width:125px"><b>Your Text Here</b><br>You can simply impress your audience and add a unique zing and appeal to your Presentations.</p>
    <div class="num" style="left:193px;top:118px">03</div>
    <p class="abs tiny" style="left:210px;top:110px;width:125px"><b>Your Text Here</b><br>You can simply impress your audience and add a unique zing and appeal to your Presentations.</p>
    <div class="num" style="left:193px;top:148px">04</div>
    <p class="abs tiny" style="left:210px;top:140px;width:125px"><b>Your Text Here</b><br>You can simply impress your audience and add a unique zing and appeal to your Presentations.</p>
    <div class="funding"><i></i>This project has received funding under Grant Agreement No 000000</div><div class="page-dot"></div>
  </section>

  <section class="slide" style="left:799px;top:1184px">
    <div class="brand">TOLMERY</div>
    <div class="title">The project</div>
    <div class="subtitle">SUB TITLE GOES HERE</div>
    <svg class="abs" style="left:38px;top:55px" width="118" height="118" viewBox="0 0 118 118">
      <g transform="rotate(-90 59 59)" fill="none" stroke-width="30">
        <circle cx="59" cy="59" r="42" stroke="var(--yellow)" stroke-dasharray="85 179" stroke-dashoffset="-2"/>
        <circle cx="59" cy="59" r="42" stroke="var(--purple)" stroke-dasharray="83 181" stroke-dashoffset="-91"/>
        <circle cx="59" cy="59" r="42" stroke="var(--purple-2)" stroke-dasharray="83 181" stroke-dashoffset="-178"/>
      </g>
      <circle cx="59" cy="59" r="10" fill="#fff"/>
    </svg>
    <div class="abs" style="left:192px;top:60px;width:18px;height:18px;border-radius:50%;background:var(--yellow)"></div>
    <p class="abs tiny" style="left:218px;top:62px;width:118px">Lorem ipsum dolor sit amet, consectetur adipiscing elit, sed do eiusmod tempor incididunt ut labore et dolore magna aliqua.</p>
    <div class="abs" style="left:192px;top:98px;width:18px;height:18px;border-radius:50%;background:var(--purple)"></div>
    <p class="abs tiny" style="left:218px;top:100px;width:118px">Lorem ipsum dolor sit amet, consectetur adipiscing elit, sed do eiusmod tempor incididunt ut labore et dolore magna aliqua.</p>
    <div class="abs" style="left:192px;top:136px;width:18px;height:18px;border-radius:50%;background:var(--purple-2)"></div>
    <p class="abs tiny" style="left:218px;top:138px;width:118px">Lorem ipsum dolor sit amet, consectetur adipiscing elit, sed do eiusmod tempor incididunt ut labore et dolore magna aliqua.</p>
    <div class="funding"><i></i>This project has received funding under Grant Agreement No 000000</div><div class="page-dot"></div>
  </section>

  <!-- Row 4 -->
  <section class="slide" style="left:48px;top:1399px">
    <div class="abs" style="left:0;top:0;width:353px;height:93px;background:linear-gradient(90deg,var(--purple-2),var(--purple-deep))"></div>
    <div class="abs" style="left:17px;top:40px;font-weight:700;font-size:13px;color:#fff">Your Text Here</div>
    <p class="abs tiny" style="left:160px;top:32px;width:180px;color:#fff">Lorem ipsum dolor sit amet, consectetur adipiscing elit, sed do eiusmod tempor incididunt ut labore et dolore magna aliqua. Ut enim ad minim veniam, quis nostrud exercitation ullamco laboris nisi ut aliquip ex ea commodo consequat. Lorem ipsum dolor sit amet, consectetur adipiscing elit.</p>
    <div class="abs" style="left:48px;top:114px;width:14px;height:14px;border:1.2px solid #333;border-radius:50%"></div>
    <p class="abs tiny" style="left:72px;top:113px;width:90px"><b style="color:var(--purple)">Lorem ipsum dolor</b><br>Lorem ipsum dolor sit amet, consectetur adipiscing elit.</p>
    <div class="abs" style="left:192px;top:114px;width:14px;height:14px;border:1.2px solid #333;border-radius:50%"></div>
    <p class="abs tiny" style="left:215px;top:113px;width:90px"><b style="color:var(--purple)">Lorem ipsum dolor</b><br>Lorem ipsum dolor sit amet, consectetur adipiscing elit.</p>
    <div class="abs" style="left:48px;top:148px;width:14px;height:14px;border:1.2px solid #333;border-radius:50%"></div>
    <p class="abs tiny" style="left:72px;top:147px;width:90px"><b style="color:var(--purple)">Lorem ipsum dolor</b><br>Lorem ipsum dolor sit amet, consectetur adipiscing elit.</p>
    <div class="abs" style="left:192px;top:148px;width:14px;height:14px;border:1.2px solid #333;border-radius:50%"></div>
    <p class="abs tiny" style="left:215px;top:147px;width:90px"><b style="color:var(--purple)">Lorem ipsum dolor</b><br>Lorem ipsum dolor sit amet, consectetur adipiscing elit.</p>
    <div class="funding"><i></i>This project has received funding under Grant Agreement No 000000</div><div class="page-dot"></div>
  </section>

  <section class="slide" style="left:423px;top:1399px">
    <div class="brand">TOLMERY</div>
    <div class="title">Training</div>
    <div class="subtitle">SUB TITLE GOES HERE</div>
    <div class="card" style="left:36px;top:78px;width:82px;height:72px"><span class="icon-ring"></span><h4>Lorem ipsum dolor</h4><p class="tiny">Lorem ipsum dolor sit amet, consectetur adipiscing elit, sed do eiusmod tempor incididunt ut labore et dolore magna aliqua.</p></div>
    <div class="card" style="left:135px;top:78px;width:82px;height:72px"><span class="icon-ring"></span><h4>Lorem ipsum dolor</h4><p class="tiny">Lorem ipsum dolor sit amet, consectetur adipiscing elit, sed do eiusmod tempor incididunt ut labore et dolore magna aliqua.</p></div>
    <div class="card" style="left:234px;top:78px;width:82px;height:72px"><span class="icon-ring"></span><h4>Lorem ipsum dolor</h4><p class="tiny">Lorem ipsum dolor sit amet, consectetur adipiscing elit, sed do eiusmod tempor incididunt ut labore et dolore magna aliqua.</p></div>
    <div class="funding"><i></i>This project has received funding under Grant Agreement No 000000</div><div class="page-dot"></div>
  </section>

  <section class="slide" style="left:799px;top:1399px">
    <div class="brand">TOLMERY</div>
    <div class="title">Training</div>
    <div class="subtitle">SUB TITLE GOES HERE</div>
    <div class="card" style="left:36px;top:62px;width:82px;height:48px"><span class="icon-ring"></span><h4>Lorem ipsum dolor</h4><p class="tiny">Lorem ipsum dolor sit amet, consectetur adipiscing elit, sed do eiusmod tempor.</p></div>
    <div class="card" style="left:135px;top:62px;width:82px;height:48px"><span class="icon-ring"></span><h4>Lorem ipsum dolor</h4><p class="tiny">Lorem ipsum dolor sit amet, consectetur adipiscing elit, sed do eiusmod tempor.</p></div>
    <div class="card" style="left:234px;top:62px;width:82px;height:48px"><span class="icon-ring"></span><h4>Lorem ipsum dolor</h4><p class="tiny">Lorem ipsum dolor sit amet, consectetur adipiscing elit, sed do eiusmod tempor.</p></div>
    <div class="card" style="left:36px;top:130px;width:82px;height:48px"><span class="icon-ring"></span><h4>Lorem ipsum dolor</h4><p class="tiny">Lorem ipsum dolor sit amet, consectetur adipiscing elit, sed do eiusmod tempor.</p></div>
    <div class="card" style="left:135px;top:130px;width:82px;height:48px"><span class="icon-ring"></span><h4>Lorem ipsum dolor</h4><p class="tiny">Lorem ipsum dolor sit amet, consectetur adipiscing elit, sed do eiusmod tempor.</p></div>
    <div class="card" style="left:234px;top:130px;width:82px;height:48px"><span class="icon-ring"></span><h4>Lorem ipsum dolor</h4><p class="tiny">Lorem ipsum dolor sit amet, consectetur adipiscing elit, sed do eiusmod tempor.</p></div>
    <div class="funding"><i></i>This project has received funding under Grant Agreement No 000000</div><div class="page-dot"></div>
  </section>

  <!-- Row 5 -->
  <section class="slide" style="left:48px;top:1613px">
    <div class="brand">TOLMERY</div>
    <div class="title">Timeline</div>
    <div class="subtitle">SUB TITLE GOES HERE</div>
    <svg class="abs" style="left:0;top:70px" width="353" height="96" viewBox="0 0 353 96" font-family="Montserrat,sans-serif" font-size="4" text-anchor="middle">
      <line x1="8" y1="48" x2="345" y2="48" stroke="#999" stroke-width="1"/>
      <g stroke-width="2" fill="#fff">
        <line x1="40" y1="20" x2="40" y2="40" stroke="var(--purple)"/><circle cx="40" cy="48" r="8" stroke="var(--purple)"/>
        <line x1="88" y1="56" x2="88" y2="76" stroke="var(--yellow)"/><circle cx="88" cy="48" r="8" stroke="var(--yellow)"/>
        <line x1="136" y1="20" x2="136" y2="40" stroke="var(--purple)"/><circle cx="136" cy="48" r="8" stroke="var(--purple)"/>
        <line x1="185" y1="56" x2="185" y2="76" stroke="var(--yellow)"/><circle cx="185" cy="48" r="8" stroke="var(--yellow)"/>
        <line x1="233" y1="20" x2="233" y2="40" stroke="var(--purple)"/><circle cx="233" cy="48" r="8" stroke="var(--purple)"/>
        <line x1="281" y1="56" x2="281" y2="76" stroke="var(--yellow)"/><circle cx="281" cy="48" r="8" stroke="var(--yellow)"/>
        <line x1="325" y1="20" x2="325" y2="40" stroke="var(--purple)"/><circle cx="325" cy="48" r="8" stroke="var(--purple)"/>
      </g>
      <g font-weight="700" fill="#333" font-size="3.6">
        <text x="40" y="49.5">2015</text><text x="88" y="49.5">2016</text><text x="136" y="49.5">2017</text><text x="185" y="49.5">2018</text><text x="233" y="49.5">2019</text><text x="281" y="49.5">2020</text><text x="325" y="49.5">2021</text>
      </g>
      <g fill="#555">
        <text x="40" y="8">Lorem ipsum dolor sit amet,</text><text x="40" y="13">consectetur adipiscing elit.</text>
        <text x="136" y="8">Lorem ipsum dolor sit amet,</text><text x="136" y="13">consectetur adipiscing elit.</text>
        <text x="233" y="8">Lorem ipsum dolor sit amet,</text><text x="233" y="13">consectetur adipiscing elit.</text>
        <text x="322" y="8">Lorem ipsum dolor sit amet,</text><text x="322" y="13">consectetur adipiscing elit.</text>
        <text x="88" y="84">Lorem ipsum dolor sit amet,</text><text x="88" y="89">consectetur adipiscing elit.</text>
        <text x="185" y="84">Lorem ipsum dolor sit amet,</text><text x="185" y="89">consectetur adipiscing elit.</text>
        <text x="281" y="84">Lorem ipsum dolor sit amet,</text><text x="281" y="89">consectetur adipiscing elit.</text>
      </g>
    </svg>
    <div class="funding"><i></i>This project has received funding under Grant Agreement No 000000</div><div class="page-dot"></div>
  </section>

  <section class="slide" style="left:423px;top:1613px">
    <div class="brand">TOLMERY</div>
    <div class="title">Timeline</div>
    <div class="subtitle">SUB TITLE GOES HERE</div>
    <svg class="abs" style="left:14px;top:70px" width="326" height="82" viewBox="0 0 326 82" font-family="Montserrat,sans-serif" text-anchor="middle" fill="#fff">
      <polygon points="0,0 58,0 72,41 58,82 0,82 12,41" fill="var(--purple)"/>
      <polygon points="62,0 120,0 134,41 120,82 62,82 76,41" fill="var(--purple-2)"/>
      <polygon points="124,0 182,0 196,41 182,82 124,82 138,41" fill="var(--lilac)"/>
      <polygon points="186,0 244,0 258,41 244,82 186,82 200,41" fill="var(--yellow)"/>
      <polygon points="248,0 306,0 320,41 306,82 248,82 262,41" fill="var(--yellow-2)"/>
      <g font-weight="700" font-size="8"><text x="38" y="26">2000</text><text x="100" y="26">2005</text><text x="162" y="26">2007</text><text x="224" y="26">2015</text><text x="286" y="26">2021</text></g>
      <g font-weight="700" font-size="3.8"><text x="38" y="46">INFODATA 01</text><text x="100" y="46">INFODATA 02</text><text x="162" y="46">INFODATA 03</text><text x="224" y="46">INFODATA 04</text><text x="286" y="46">INFODATA 05</text></g>
      <g font-size="3.4"><text x="38" y="53">Lorem ipsum dolor</text><text x="38" y="58">sit amet, elit</text><text x="100" y="53">Lorem ipsum dolor</text><text x="100" y="58">sit amet, elit</text><text x="162" y="53">Lorem ipsum dolor</text><text x="162" y="58">sit amet, elit</text><text x="224" y="53">Lorem ipsum dolor</text><text x="224" y="58">sit amet, elit</text><text x="286" y="53">Lorem ipsum dolor</text><text x="286" y="58">sit amet, elit</text></g>
    </svg>
    <div class="funding"><i></i>This project has received funding under Grant Agreement No 000000</div><div class="page-dot"></div>
  </section>

  <section class="slide" style="left:799px;top:1613px">
    <div class="brand">TOLMERY</div>
    <div class="title">Our Sponsors</div>
    <div class="subtitle">SUB TITLE GOES HERE</div>
    <div class="badge" style="left:40px;top:78px"><i style="background:#e07a2e"></i></div>
    <div class="badge" style="left:88px;top:78px"><i style="background:#9cc6a6;width:9px;height:11px"></i></div>
    <div class="badge" style="left:136px;top:78px"><i style="background:#1e55a8;width:10px;height:10px;border-radius:50%"></i></div>
    <div class="badge" style="left:184px;top:78px"><i style="background:#333"></i></div>
    <div class="badge" style="left:232px;top:78px"><i style="background:#ccc;height:3px"></i></div>
    <div class="badge" style="left:280px;top:78px"><i style="background:#3aa0e0"></i></div>
    <div class="badge" style="left:40px;top:115px"><i style="background:#7ab648;width:8px;height:8px"></i></div>
    <div class="badge" style="left:88px;top:115px"><i style="background:#e04b1f;width:8px;height:8px"></i></div>
    <div class="badge" style="left:136px;top:115px"><i style="background:#222;height:4px"></i></div>
    <div class="badge" style="left:184px;top:115px"><i style="background:#333"></i></div>
    <div class="badge" style="left:232px;top:115px"><i style="background:#ccc;height:3px"></i></div>
    <div class="badge" style="left:280px;top:115px"><i style="background:#3aa0e0"></i></div>
    <div class="funding"><i></i>This project has received funding under Grant Agreement No 000000</div><div class="page-dot"></div>
  </section>

  <!-- Row 6 -->
  <section class="slide" style="left:48px;top:1827px">
    <div class="brand">TOLMERY</div>
    <div class="title">Your Text Here</div>
    <div class="subtitle">SUB TITLE GOES HERE</div>
    <svg class="abs" style="left:100px;top:52px" width="160" height="136" viewBox="0 0 160 136" font-family="Montserrat,sans-serif" font-size="5" font-weight="600" fill="#fff" text-anchor="middle">
      <polygon points="63,6 97,6 104,24 56,24" fill="var(--purple-2)"/>
      <polygon points="52,30 108,30 100,48 48,48" fill="var(--yellow-2)"/>
      <polygon points="44,54 116,54 124,72 36,72" fill="var(--purple-2)"/>
      <polygon points="32,78 128,78 120,96 24,96" fill="var(--yellow-2)"/>
      <polygon points="20,102 140,102 150,120 10,120" fill="var(--purple-2)"/>
      <text x="80" y="17">Idea 05</text><text x="80" y="41">Idea 04</text><text x="80" y="65">Idea 03</text><text x="80" y="89">Idea 02</text><text x="80" y="113">Idea 01</text>
    </svg>
    <div class="funding"><i></i>This project has received funding under Grant Agreement No 000000</div><div class="page-dot"></div>
  </section>

  <section class="slide" style="left:423px;top:1827px">
    <div class="brand">TOLMERY</div>
    <div class="title" style="top:24px">Your Text Here</div>
    <div class="subtitle" style="top:43px">SUB TITLE GOES HERE</div>
    <div class="abs" style="left:18px;top:80px;width:118px;height:62px;border-radius:6px;background:var(--purple)">
      <div style="text-align:center;color:#fff;font-size:5px;font-weight:700;margin-top:7px">Lorem ipsum dolor sit</div>
      <svg style="position:absolute;left:10px;top:22px" width="105" height="32" viewBox="0 0 105 32" font-family="Montserrat,sans-serif" font-size="4" fill="#fff">
        <g fill="var(--yellow)"><rect x="0" y="2" width="3" height="8"/><rect x="5" y="2" width="3" height="8"/><rect x="10" y="2" width="3" height="8"/><rect x="15" y="2" width="3" height="8"/><rect x="20" y="2" width="3" height="8"/><rect x="25" y="2" width="3" height="8"/></g>
        <g fill="#c9c2ea"><rect x="30" y="2" width="3" height="8"/><rect x="35" y="2" width="3" height="8"/><rect x="40" y="2" width="3" height="8"/><rect x="45" y="2" width="3" height="8"/></g>
        <g fill="var(--yellow)"><rect x="0" y="18" width="3" height="8"/><rect x="5" y="18" width="3" height="8"/><rect x="10" y="18" width="3" height="8"/><rect x="15" y="18" width="3" height="8"/></g>
        <g fill="#c9c2ea"><rect x="20" y="18" width="3" height="8"/><rect x="25" y="18" width="3" height="8"/><rect x="30" y="18" width="3" height="8"/><rect x="35" y="18" width="3" height="8"/><rect x="40" y="18" width="3" height="8"/><rect x="45" y="18" width="3" height="8"/></g>
        <text x="62" y="8">60% Male</text><text x="62" y="24">40% Female</text>
      </svg>
    </div>
    <div class="abs" style="left:160px;top:88px;width:1px;height:48px;background:#555"></div>
    <div class="abs" style="left:166px;top:85px;color:var(--purple);font-size:8px;font-weight:500">22 Mill.</div>
    <p class="abs tiny" style="left:166px;top:96px;width:60px">Lorem ipsum dolor sit amet, consectetur amet</p>
    <div class="abs" style="left:166px;top:113px;color:var(--purple);font-size:8px;font-weight:500">4.3 Bill.</div>
    <p class="abs tiny" style="left:166px;top:124px;width:60px">Lorem ipsum dolor sit amet, consectetur amet</p>
    <div class="abs" style="left:260px;top:88px;width:1px;height:48px;background:#555"></div>
    <div class="abs" style="left:266px;top:85px;color:var(--purple);font-size:8px;font-weight:500">20</div>
    <p class="abs tiny" style="left:266px;top:96px;width:60px">Lorem ipsum dolor sit amet, consectetur amet</p>
    <div class="abs" style="left:266px;top:113px;color:var(--purple);font-size:8px;font-weight:500">4.1%</div>
    <p class="abs tiny" style="left:266px;top:124px;width:60px">Lorem ipsum dolor sit amet, consectetur amet</p>
    <div class="funding"><i></i>This project has received funding under Grant Agreement No 000000</div><div class="page-dot"></div>
  </section>

  <section class="slide" style="left:799px;top:1827px">
    <div class="brand">TOLMERY</div>
    <div class="title" style="top:12px">Table</div>
    <div class="subtitle" style="top:30px">SUB TITLE GOES HERE</div>
    <table class="grid-table" style="left:18px;top:48px;width:317px">
      <tr><th></th><th>Content</th><th>Content</th><th>Content</th><th>Content</th><th>Content</th></tr>
      <tr><td>Text Here</td><td>Text Here</td><td>Text Here</td><td>Text Here</td><td>Text Here</td><td>Text Here</td></tr>
      <tr><td>Content</td><td>Content</td><td>Content</td><td>Content</td><td>Content</td><td>Content</td></tr>
      <tr><td>Text Here</td><td>Text Here</td><td>Text Here</td><td>Text Here</td><td>Text Here</td><td>Text Here</td></tr>
      <tr><td>Content</td><td>Content</td><td>Content</td><td>Content</td><td>Content</td><td>Content</td></tr>
      <tr class="accent"><td>Text Here</td><td>Text Here</td><td>Text Here</td><td>Text Here</td><td>Text Here</td><td>Text Here</td></tr>
    </table>
    <div class="abs" style="left:18px;top:172px;width:317px;height:11px;background:var(--yellow);color:#fff;font-size:4px;font-weight:600;text-align:center;line-height:11px">You can simply impress your audience and add a unique zing</div>
    <div class="funding"><i></i>This project has received funding under Grant Agreement No 000000</div><div class="page-dot"></div>
  </section>

  <!-- Row 7 -->
  <section class="slide" style="left:48px;top:2042px">
    <div class="brand">TOLMERY</div>
    <div class="title" style="top:12px">Table</div>
    <div class="subtitle" style="top:30px">SUB TITLE GOES HERE</div>
    <div class="abs" style="left:0;top:44px;width:26px;height:28px;background:var(--purple)"></div>
    <table class="grid-table" style="left:26px;top:44px;width:327px">
      <tr><th colspan="12" style="background:var(--purple)">MONTHS</th></tr>
      <tr><td style="background:#d9d6ec">1</td><td style="background:#d9d6ec">2</td><td style="background:#d9d6ec">3</td><td style="background:#d9d6ec">4</td><td style="background:#d9d6ec">5</td><td style="background:#d9d6ec">6</td><td style="background:#d9d6ec">7</td><td style="background:#d9d6ec">8</td><td style="background:#d9d6ec">9</td><td style="background:#d9d6ec">10</td><td style="background:#d9d6ec">11</td><td style="background:#d9d6ec">12</td></tr>
    </table>
    <div class="abs" style="left:0;top:90px;width:353px;height:19px;background:#f0f0f1"></div>
    <div class="abs" style="left:0;top:128px;width:353px;height:19px;background:#f0f0f1"></div>
    <div class="abs" style="left:0;top:166px;width:353px;height:19px;background:#f0f0f1"></div>
    <div class="abs tiny" style="left:8px;top:72px;line-height:19px">P-1<br>P-2<br>P-3<br>P-4<br>P-5<br>P-6</div>
    <div class="funding"><i></i>This project has received funding under Grant Agreement No 000000</div><div class="page-dot"></div>
  </section>

  <section class="slide" style="left:423px;top:2042px">
    <div class="brand">TOLMERY</div>
    <div class="title" style="top:12px">Table</div>
    <div class="subtitle" style="top:30px">SUB TITLE GOES HERE</div>
    <svg class="abs" style="left:22px;top:58px" width="306" height="110" viewBox="0 0 306 110" font-family="Montserrat,sans-serif" font-size="3.6">
      <rect x="60" y="0" width="246" height="8" fill="#fff" stroke="var(--purple)" stroke-width=".6"/>
      <g fill="#333" text-anchor="middle">
        <text x="64" y="6">M</text><text x="73" y="6">T</text><text x="82" y="6">W</text><text x="91" y="6">T</text><text x="100" y="6">F</text><text x="109" y="6">S</text><text x="118" y="6">S</text><text x="127" y="6">M</text><text x="136" y="6">T</text><text x="145" y="6">W</text><text x="154" y="6">T</text><text x="163" y="6">F</text><text x="172" y="6">S</text><text x="181" y="6">S</text><text x="190" y="6">M</text><text x="199" y="6">T</text><text x="208" y="6">W</text><text x="217" y="6">T</text><text x="226" y="6">F</text><text x="235" y="6">S</text><text x="244" y="6">S</text><text x="253" y="6">M</text><text x="262" y="6">T</text><text x="271" y="6">W</text><text x="280" y="6">T</text><text x="289" y="6">F</text><text x="298" y="6">S</text>
      </g>
      <rect x="0" y="10" width="306" height="7" fill="var(--purple-2)"/>
      <g fill="#fff" text-anchor="middle" font-weight="600"><text x="30" y="15">WEEK X</text><text x="92" y="15">WEEK 1</text><text x="153" y="15">WEEK 2</text><text x="214" y="15">WEEK 3</text><text x="275" y="15">WEEK 4</text></g>
      <g fill="#333"><text x="2" y="26">Task 1</text><text x="2" y="38">Task 2</text><text x="2" y="50">Task 3</text><text x="2" y="62">Task 4</text><text x="2" y="74">Task 5</text><text x="2" y="86">Task 6</text></g>
      <g stroke="#eee" stroke-width=".6"><line x1="0" y1="29" x2="306" y2="29"/><line x1="0" y1="41" x2="306" y2="41"/><line x1="0" y1="53" x2="306" y2="53"/><line x1="0" y1="65" x2="306" y2="65"/><line x1="0" y1="77" x2="306" y2="77"/></g>
      <rect x="60" y="20" width="120" height="8" fill="#d9d6ec"/>
      <rect x="66" y="32" width="74" height="8" fill="#8c8c92"/>
      <rect x="152" y="44" width="80" height="8" fill="var(--purple)"/>
      <rect x="165" y="56" width="80" height="8" fill="var(--yellow)"/>
      <rect x="134" y="68" width="172" height="8" fill="#9c9ca2"/>
      <rect x="254" y="80" width="52" height="8" fill="var(--purple)"/>
    </svg>
    <div class="funding"><i></i>This project has received funding under Grant Agreement No 000000</div><div class="page-dot"></div>
  </section>

  <section class="slide" style="left:799px;top:2042px">
    <div class="brand">TOLMERY</div>
    <div class="title" style="top:12px">Demographic</div>
    <div class="subtitle" style="top:30px">SUB TITLE GOES HERE</div>
    <svg class="abs" style="left:22px;top:75px" width="320" height="95" viewBox="0 0 320 95" font-family="Montserrat,sans-serif">
      <polyline points="2,10 7,16 2,22" fill="none" stroke="var(--purple)" stroke-width="2.5"/>
      <polyline points="2,56 7,62 2,68" fill="none" stroke="var(--yellow)" stroke-width="2.5"/>
      <g font-size="4" fill="#444"><text x="14" y="8" font-weight="700">Male Population</text><text x="14" y="13">You can simply impress your audience and add a</text><text x="14" y="18">unique zing and appeal to your Presentations.</text><text x="14" y="23">Easy to change colors, photos and Text.</text>
      <text x="14" y="54" font-weight="700">Female Population</text><text x="14" y="59">You can simply impress your audience and add a</text><text x="14" y="64">unique zing and appeal to your Presentations.</text><text x="14" y="69">Easy to change colors, photos and Text.</text></g>
      <polygon points="155,6 178,6 186,16 178,26 155,26" fill="#333"/><text x="166" y="18" font-size="5" fill="#fff" font-weight="700" text-anchor="middle">40%</text>
      <polygon points="155,52 178,52 186,62 178,72 155,72" fill="#333"/><text x="166" y="64" font-size="5" fill="#fff" font-weight="700" text-anchor="middle">80%</text>
      <g fill="var(--purple)"><rect x="196" y="6" width="7" height="20" rx="2"/><rect x="208" y="6" width="7" height="20" rx="2"/><rect x="220" y="6" width="7" height="20" rx="2"/><rect x="232" y="6" width="7" height="20" rx="2"/></g>
      <g fill="#333"><rect x="244" y="6" width="7" height="20" rx="2"/><rect x="256" y="6" width="7" height="20" rx="2"/><rect x="268" y="6" width="7" height="20" rx="2"/><rect x="280" y="6" width="7" height="20" rx="2"/><rect x="292" y="6" width="7" height="20" rx="2"/><rect x="304" y="6" width="7" height="20" rx="2"/></g>
      <g fill="var(--yellow)"><rect x="196" y="52" width="7" height="20" rx="2"/><rect x="208" y="52" width="7" height="20" rx="2"/><rect x="220" y="52" width="7" height="20" rx="2"/><rect x="232" y="52" width="7" height="20" rx="2"/><rect x="244" y="52" width="7" height="20" rx="2"/><rect x="256" y="52" width="7" height="20" rx="2"/><rect x="268" y="52" width="7" height="20" rx="2"/><rect x="280" y="52" width="7" height="20" rx="2"/></g>
      <g fill="#333"><rect x="292" y="52" width="7" height="20" rx="2"/><rect x="304" y="52" width="7" height="20" rx="2"/></g>
    </svg>
    <div class="funding"><i></i>This project has received funding under Grant Agreement No 000000</div><div class="page-dot"></div>
  </section>

  <!-- Row 8 -->
  <section class="slide" style="left:423px;top:2249px;background:linear-gradient(#f4f3f9,#fff 45%)">
    <div class="photo" role="img" aria-label="Faded photo of a woman speaking into a megaphone" style="left:0;top:0;width:130px;height:95px;background:radial-gradient(ellipse at 40% 40%,#e8dfe0,#f4f3f9 70%)"></div>
    <div class="abs" style="left:116px;top:40px;font-size:19px;color:var(--purple)"><b style="font-weight:800">THANK</b> <span style="font-weight:400">YOU</span></div>
    <svg class="abs" style="left:40px;top:112px" width="10" height="62" viewBox="0 0 10 62" fill="var(--purple)">
      <path d="M2 1 L4 1 L5 4 L4 5 Q5 7 7 8 L8 7 L10 8 L10 10 Q6 11 3 7 Q1 4 2 1Z"/>
      <circle cx="5" cy="23" r="4" fill="none" stroke="var(--purple)" stroke-width="1.2"/><line x1="1" y1="23" x2="9" y2="23" stroke="var(--purple)" stroke-width=".8"/>
      <rect x="1" y="38" width="8" height="6" rx="1"/><polyline points="1,38 5,42 9,38" fill="none" stroke="#fff" stroke-width=".8"/>
      <path d="M5 52 a3.5 3.5 0 0 1 3.5 3.5 Q8.5 58 5 62 Q1.5 58 1.5 55.5 A3.5 3.5 0 0 1 5 52Z"/>
    </svg>
    <div class="abs tiny" style="left:56px;top:114px;line-height:16.5px;font-size:4.5px;color:#333">555.014.2290<br>www.tolmery.example<br>info@tolmery.example<br>Here to write your Company adress</div>
    <div class="abs" style="left:237px;top:114px;display:grid;grid-template-columns:9px auto;gap:7px 6px;font-size:4.5px;color:#333;align-items:center">
      <i style="width:8px;height:8px;border-radius:50%;background:var(--purple)"></i><span>Name</span>
      <i style="width:8px;height:8px;border-radius:50%;background:var(--purple)"></i><span>Name</span>
      <i style="width:8px;height:8px;border-radius:50%;background:var(--purple)"></i><span>Name</span>
      <i style="width:8px;height:8px;border-radius:50%;background:var(--purple)"></i><span>Name</span>
    </div>
  </section>

  <section class="slide" style="left:799px;top:2249px">
    <div class="brand">TOLMERY</div>
    <div class="title" style="top:12px">Bullet Point</div>
    <div class="subtitle" style="top:30px">TWO CULLUM</div>
    <ul class="bullets" style="left:35px;top:50px;width:130px">
      <li>Lorem ipsum dolor sit amet, no consectetur adipiscing elit, sed do eiusmod ti mo tempor</li>
      <li>Lorem ipsum dolor sit amet, no consectetur adipiscing elit, sed do eiusmod ti mo tempor</li>
      <li>Lorem ipsum dolor sit amet, no consectetur adipiscing elit, sed do eiusmod ti mo tempor</li>
      <li>Lorem ipsum dolor sit amet, no consectetur adipiscing elit, sed do eiusmod ti mo tempor</li>
      <li>Lorem ipsum dolor sit amet, no consectetur adipiscing elit, sed do eiusmod ti mo tempor</li>
      <li>Lorem ipsum dolor sit amet, no consectetur adipiscing elit, sed do eiusmod ti mo tempor</li>
    </ul>
    <ul class="bullets" style="left:192px;top:50px;width:130px">
      <li>Lorem ipsum dolor sit amet, no consectetur adipiscing elit, sed do eiusmod ti mo tempor</li>
      <li>Lorem ipsum dolor sit amet, no consectetur adipiscing elit, sed do eiusmod ti mo tempor</li>
      <li>Lorem ipsum dolor sit amet, no consectetur adipiscing elit, sed do eiusmod ti mo tempor</li>
      <li>Lorem ipsum dolor sit amet, no consectetur adipiscing elit, sed do eiusmod ti mo tempor</li>
      <li>Lorem ipsum dolor sit amet, no consectetur adipiscing elit, sed do eiusmod ti mo tempor</li>
    </ul>
    <div class="funding"><i></i>This project has received funding under Grant Agreement No 000000</div><div class="page-dot"></div>
  </section>

</main>
</body>
</html>
```